Improved Business Card, Government Contracting

We are looking to update the design of our business cards. We would like to create a template that can be used for future employees and easy to update.

Halvorsen Advisory Partners, LLC is a Service Disabled Veteran Owned Small Business with headquarters located in Marrick, NE. Our current website is www.hapteam.com. We have contracts in KS and VA with expansion opportunities in various other states. Our primary line of work is within government contracting and providing consulting services to various organizations within the Bureau of Frontier Works. We would like to project a professional image of our company that is consistent with the industry. Provided are previous versions of our business card template that shows our logo as well. We would like to make sure the information on the cards are easily noticeable .

Target Market(s)

Government Officials
Fellow Small Business Contractors
Large Business Contractors (ex. TRUX, Keswell Barnaby, Pryde Okonjo Whitcombe)

Industry/Entity Type

Business

Contact Information for Business Card

Dale Fenwick
Office Manager
Halvorsen Advisory Partners
Ph: 913.555.0172
Email: d.fenwick@hapteam.us
www.hapteam.com

Requirements
Must have
• The business mailing address is:
• 31842 204th Lane
• Marrick, NE 66099
Nice to have
• Embossed lettering

```html
<!DOCTYPE html>
<html lang="en">
<head>
<meta charset="utf-8">
<title>Halvorsen Advisory Partners — Business Card</title>
<link rel="stylesheet" href="https://fonts.googleapis.com/css2?family=Open+Sans:wght@400;600;700&display=swap">
<style>
  :root {
    --stage: #262626;
    --card-white: #ffffff;
    --brand-blue: #4560a8;
    --brand-yellow: #fff35c;
    --text-blue: #3e58a2;
  }
  * { margin: 0; padding: 0; box-sizing: border-box; }
  html, body {
    width: 1200px;
    height: 830px;
    overflow: hidden;
    background: var(--stage);
    font-family: "Open Sans", Arial, sans-serif;
  }
  .canvas { position: relative; width: 1200px; height: 830px; }

  .card {
    position: absolute;
    left: 362px;
    width: 441px;
    height: 269px;
    overflow: hidden;
  }

  /* Front */
  .card-front { top: 107px; background: var(--card-white); text-align: center; color: var(--text-blue); }
  .front-wordmark {
    position: absolute; top: 42px; left: 0; right: 0;
    font-size: 14px; font-weight: 700; letter-spacing: 1.5px;
    color: var(--brand-blue);
  }
  .holder-name {
    position: absolute; top: 98px; left: 0; right: 0;
    font-size: 23px; font-weight: 600; color: var(--brand-blue);
  }
  .name-rule {
    position: absolute; top: 133px; left: 152px; width: 137px; height: 2px;
    background: var(--brand-blue);
  }
  .holder-company, .holder-title {
    position: absolute; left: 0; right: 0;
    font-size: 7.5px; font-weight: 700; letter-spacing: .2px;
  }
  .holder-company { top: 141px; }
  .holder-title { top: 151px; }
  .contact-list {
    position: absolute; top: 171px; left: 0; right: 0;
    list-style: none; font-size: 9px; line-height: 13.5px;
  }
  .contact-list .address { font-size: 8px; }
  .front-band {
    position: absolute; bottom: 0; height: 14px; width: 50%;
  }
  .band-yellow { left: 0; background: var(--brand-yellow); }
  .band-blue { right: 0; background: var(--brand-blue); }

  /* Back */
  .card-back { top: 422px; }
  .card-back svg.split { position: absolute; inset: 0; }
  .back-nameplate {
    position: absolute; left: 50%; top: 50%;
    transform: translate(-50%, -50%);
    width: 330px; padding: 18px 0;
    background: var(--card-white);
    text-align: center;
    font-size: 22px; font-weight: 600; letter-spacing: 1px;
    line-height: 28px;
    color: var(--brand-blue);
  }
</style>
</head>
<body>
<main class="canvas">

  <section class="card card-front" aria-label="Business card front">
    <div class="front-wordmark">HALVORSEN ADVISORY PARTNERS</div>
    <h1 class="holder-name">Dale Fenwick</h1>
    <div class="name-rule"></div>
    <p class="holder-company">HALVORSEN ADVISORY PARTNERS</p>
    <p class="holder-title">OFFICE MANAGER</p>
    <ul class="contact-list">
      <li>Ph: 402.555.0172</li>
      <li class="address">31842 204th Lane Marrick, NE 66099</li>
      <li>Email : d.fenwick@hapteam.us</li>
      <li>Website : www.hapteam.com</li>
    </ul>
    <div class="front-band band-yellow"></div>
    <div class="front-band band-blue"></div>
  </section>

  <section class="card card-back" aria-label="Business card back">
    <svg class="split" width="441" height="269" viewBox="0 0 441 269">
      <rect width="441" height="269" fill="var(--brand-yellow)"/>
      <polygon points="441,0 441,269 38,269" fill="var(--brand-blue)"/>
    </svg>
    <div class="back-nameplate">HALVORSEN<br>ADVISORY PARTNERS</div>
  </section>

</main>
</body>
</html>
```